60 Ways to de-stress Poster

I would like a poster ( A4 full colour) with a list of 60 ways to destress. I would like the design to be clean and stylish (not cartoonish)

My Target market is stressed out mums so I want the poster to feel inspirational and relaxing to look at.

I have added a sample of something I like - but open to other ideas

Finished art would be print ready pdf

Target Market(s)

Mums who are stressed out - mainly new mums. I want this to be a poster that someone would happily put up that looks more like artwork.

Requirements
Must have
• My logo elements and colours but happy to incorporate other colours that blend well into it.

Colours:
Bright green: Pantone 376
Bright green as CMYK: c: 45.2% m: 0% y: 100% k: 0%

Logo text large grey: 70% black
Logo text strapline: 75% black
Tree: 80% black

Fonts:
Logo 'Willowbrook Calm': Verdana
Logo 'Counselling & coaching services for mums': Gill Sans Light
Should not have
• No cartoonish images - I want it very clean and stylish

```html
<!DOCTYPE html>
<html lang="en">
<head>
<meta charset="utf-8">
<title>60 Ways to De Stress – Poster</title>
<link href="https://fonts.googleapis.com/css2?family=Cabin:wght@400;700&family=Delius&family=Mulish:wght@700&family=Lato:wght@300&display=swap" rel="stylesheet">
<style>
  :root{
    --green:#9dc94a;
    --white:#ffffff;
    --grey:#535353;
    --magenta:#b3237d;
    --logo-grey:#4d4d4d;
    --strap-grey:#404040;
    --page:#ffffff;
  }
  html,body{margin:0;padding:0;width:1200px;height:1000px;overflow:hidden;background:var(--page);}
  .canvas{position:relative;width:1200px;height:1000px;overflow:hidden;}
  .poster{position:absolute;left:267px;top:50px;width:638px;height:900px;background:var(--page);}
  .poster__field{position:absolute;left:0;top:0;width:638px;height:803px;background:var(--green);}
  .title{position:absolute;margin:0;color:var(--white);font-family:"Cabin",sans-serif;line-height:1;}
  .title__number{position:absolute;left:68px;top:14px;font-size:132px;font-weight:700;letter-spacing:-6px;}
  .title__line{position:absolute;left:243px;white-space:nowrap;}
  .title__line--top{top:32px;font-size:58px;font-weight:700;letter-spacing:1px;}
  .title__line--bottom{top:84px;font-size:56px;font-weight:400;letter-spacing:1px;}

  .ways{list-style:none;margin:0;padding:0;}
  .way{position:absolute;font-family:"Delius",sans-serif;white-space:nowrap;line-height:1.05;}
  .way--white{color:var(--white);}
  .way--grey{color:var(--grey);}
  .way--magenta{color:var(--magenta);}
  .way--up{writing-mode:vertical-rl;transform:rotate(180deg);}
  .way__small{font-size:18px;}

  .brand{position:absolute;left:279px;top:820px;}
  .brand__name{font-family:"Mulish",sans-serif;font-weight:700;font-size:25px;color:var(--logo-grey);margin:0;white-space:nowrap;}
  .brand__strap{font-family:"Lato",sans-serif;font-weight:300;font-size:15px;color:var(--strap-grey);margin:2px 0 0;white-space:nowrap;}
  .brand__dot{position:absolute;left:240px;top:8px;width:22px;height:22px;border-radius:50%;background:var(--green);}
</style>
</head>
<body>
<div class="canvas">
  <section class="poster">
    <div class="poster__field">
      <h1 class="title">
        <span class="title__number">60</span>
        <span class="title__line title__line--top">WAYS TO</span>
        <span class="title__line title__line--bottom">DE STRESS</span>
      </h1>

      <ul class="ways">
        <li class="way way--white" style="left:188px;top:156px;font-size:26px">put on some music and dance</li>
        <li class="way way--magenta" style="left:200px;top:190px;font-size:21px">light a scented candle</li>
        <li class="way way--magenta" style="left:447px;top:191px;font-size:14px">write a poem</li>
        <li class="way way--grey" style="left:192px;top:220px;font-size:18px">take a mini mental holiday</li>
        <li class="way way--white" style="left:446px;top:211px;font-size:17px">fake a smile</li>
        <li class="way way--grey" style="left:449px;top:234px;font-size:16px">gaze at the</li>
        <li class="way way--grey" style="left:451px;top:246px;font-size:36px">stars</li>
        <li class="way way--white" style="left:184px;top:245px;font-size:18px">swing on a swing</li>
        <li class="way way--magenta" style="left:333px;top:250px;font-size:13px">hug someone</li>
        <li class="way way--magenta" style="left:153px;top:270px;font-size:14px">go to the park</li>
        <li class="way way--white" style="left:254px;top:270px;font-size:13px">take a nap</li>
        <li class="way way--grey" style="left:347px;top:272px;font-size:15px">write in<br>a journal</li>
        <li class="way way--white" style="left:445px;top:286px;font-size:21px">pat a dog</li>
        <li class="way way--grey" style="left:137px;top:292px;font-size:22px">listening to music</li>
        <li class="way way--white way--up" style="left:416px;top:165px;height:225px;font-size:22px">make a gratitude list</li>
        <li class="way way--magenta way--up" style="left:327px;top:268px;height:120px;font-size:13px">call or visit a friend</li>
        <li class="way way--white" style="left:173px;top:322px;font-size:16px">buy yourself flowers</li>
        <li class="way way--magenta" style="left:346px;top:319px;font-size:16px">meditate</li>
        <li class="way way--magenta" style="left:443px;top:315px;font-size:19px">volunteer<br>your time</li>
        <li class="way way--white" style="left:346px;top:338px;font-size:28px">have</li>
        <li class="way way--white" style="left:347px;top:368px;font-size:20px">a bath</li>
        <li class="way way--grey" style="left:442px;top:360px;font-size:15px">make yourself<br>a cup of tea</li>
        <li class="way way--grey" style="left:163px;top:344px;font-size:14px">take some deep breaths</li>
        <li class="way way--magenta" style="left:136px;top:361px;font-size:30px">go for a walk</li>
        <li class="way way--white way--up" style="left:111px;top:360px;height:170px;font-size:17px">watch the clouds go by</li>
        <li class="way way--grey way--up" style="left:134px;top:420px;height:110px;font-size:11px">stand up and stretch</li>
        <li class="way way--grey" style="left:155px;top:400px;font-size:16px">plant a tree</li>
        <li class="way way--white" style="left:248px;top:398px;font-size:17.5px">eat something mindfully</li>
        <li class="way way--magenta" style="left:436px;top:406px;font-size:13px">play in the park</li>
        <li class="way way--white" style="left:157px;top:424px;font-size:19px">paint a picture</li>
        <li class="way way--grey" style="left:286px;top:424px;font-size:19px">forgive someone</li>
        <li class="way way--grey" style="left:439px;top:427px;font-size:13px">get a massage</li>
        <li class="way way--grey" style="left:156px;top:451px;font-size:16px">review your achievements</li>
        <li class="way way--white" style="left:409px;top:446px;font-size:20px">get a haircut</li>
        <li class="way way--white" style="left:156px;top:478px;font-size:18px">take a long drive</li>
        <li class="way way--grey" style="left:300px;top:470px;font-size:24px;line-height:0.9">create<br>some<br><span class="way__small">routines</span></li>
        <li class="way way--magenta way--up" style="left:385px;top:450px;height:90px;font-size:13px">go for a bike ride</li>
        <li class="way way--grey" style="left:409px;top:472px;font-size:13px">colour in a picture</li>
        <li class="way way--magenta" style="left:409px;top:490px;font-size:19px">take a class<br>at the gym</li>
        <li class="way way--grey way--up" style="left:520px;top:470px;height:150px;font-size:15px">watch a funny movie</li>
        <li class="way way--grey" style="left:157px;top:503px;font-size:24px">read a book</li>
        <li class="way way--white" style="left:110px;top:537px;font-size:20px">play a game</li>
        <li class="way way--magenta" style="left:234px;top:539px;font-size:17px">bake some cookies</li>
        <li class="way way--grey" style="left:409px;top:543px;font-size:14px">go on a picnic</li>
        <li class="way way--grey" style="left:113px;top:565px;font-size:14.5px">perform &nbsp;an act of kindness</li>
        <li class="way way--white" style="left:303px;top:565px;font-size:14px">give yourself a time-out</li>
        <li class="way way--magenta" style="left:469px;top:561px;font-size:19px">vent</li>
        <li class="way way--white" style="left:131px;top:589px;font-size:15px">listen to a guided relaxation mp3</li>
        <li class="way way--grey" style="left:384px;top:584px;font-size:24px">ask for help</li>
        <li class="way way--grey" style="left:130px;top:612px;font-size:22px">disconnect from technology</li>
        <li class="way way--magenta" style="left:428px;top:620px;font-size:14px">live for today</li>
        <li class="way way--magenta way--up" style="left:107px;top:590px;height:175px;font-size:17px">de-clutter a drawer</li>
        <li class="way way--magenta" style="left:129px;top:646px;font-size:15px">look at a work of art</li>
        <li class="way way--white" style="left:281px;top:639px;font-size:22px">visit a farmers market</li>
        <li class="way way--white" style="left:129px;top:668px;font-size:16px">borrow &nbsp;a book from the library</li>
        <li class="way way--magenta" style="left:367px;top:671px;font-size:13px">accept what you can't change</li>
        <li class="way way--grey" style="left:130px;top:691px;font-size:15px">scale down your to do list</li>
        <li class="way way--white" style="left:328px;top:691px;font-size:15px">write positive self-statements</li>
        <li class="way way--grey" style="left:129px;top:714px;font-size:17px">outsource if you can</li>
        <li class="way way--magenta" style="left:303px;top:714px;font-size:15px">try progressive muscle relaxation</li>
        <li class="way way--white" style="left:131px;top:735px;font-size:28px">compliment yourself often</li>
      </ul>
    </div>

    <footer class="brand">
      <p class="brand__name">Willowbrook Calm</p>
      <p class="brand__strap">counselling &amp; coaching for mums</p>
      <span class="brand__dot" aria-hidden="true"></span>
    </footer>
  </section>
</div>
</body>
</html>
```